Velvet Getaway Fest

I am looking for a poster design for my festival inspired by the movie Velvet Getaway starring Howard Pemberly and Lorraine Vickham. It needs to be 11x17 in 300 DPI or higher. This will be printed with digital printing so the design can't be crazy colorful or intricate in design. Backgrounds should be more on the simplistic side. It can be vertical or horizontal. It can't have exact likenesses of the actors nor do I really want to go in that direction. I prefer the "artsy" type of image. If you've never seen the film, you are probably not a fit for my project. I'm looking for someone who will put some love into this. I've attached some images of other artists designs that I kind of like so you understand the direction I want to go in. I also had an idea of some faceless characters that would only wear the characters signature sunglasses and clothes (I have attached an image, that is similar to what I mean). I am open to ideas, just make it COOL. If I love it I would probably use you again for next year's Fest. It should include the words "VELVET GETAWAY FEST"

It can also include "CORAL LODGE - BURBANK, CA. MAY 2-3, 2014". NOT 100% necessary it it kills your design, but the name of the Fest must be in there. You could also just do the location without the dates. I already have 1 print designed and I'm looking for a new one.

You also could use the Coral Lodge sign, but also not necessary, just giving you some ideas. I added a pic below

UPDATE:

For those who haven't joined this project yet or may want to submit another design, I might add a 2nd and 3rd place, also I have 1 more design idea. I have uploaded 2 images. I was thinking of a "pinup style" cartoon characters of Desmond and Georgette. I couldn't find an example that I liked for Desmond but here are some similar styles that could be used for Georgette. You need to make both Desmond and Georgette in a similar style. I could be full figure or half figure. You could re-create a famous scene from the movie or you can just pose them. They should be in their main costumes from the film and have their sunglasses on
Updates

Thanks to everyone who participated. We couldn't decide which one we liked best so we created a 2nd place and bought them both. Both were created by the same artist Tavo Lenric Obando!  Congrats!

Special mention to K. Velmot (We liked it but I think it was a little more feminine for our male crowd), Tomas Ebert (We liked it, but decided on another, sorry!), Ansel (I wished you would have sent me the revision), Pfelton Studio (A True Fan) and Marko Vuslek (most original idea but I don't think it was a fit)

Target Market(s)

This would be for 28-45 somethings

Industry/Entity Type

Festival

Colors
eb1f27
fece3e
32a6d7
e34297

Requirements
Must have
• "VELVET GETAWAY FEST" as the title of the piece in a style that fits the image or the bullet-font shown below would be my preference, but not 100% necessary.
Nice to have
• There is a bullet-riddled font that was used on the DVD. It would be cool if I could get VELVET GETAWAY FEST in that same type font with bullet holes and all. At the very least the font style should be the same. Please design something that is open to font change if I don't like it. You can do something that matched the style of your art but be prepared to change if I'm not crazy about it. Thx!

The colors I chose above are just suggestions.
Should not have
• No exact liknesses to the actors. Caricatures/cartoons etc would be fine if you went in that direction

```html
<!DOCTYPE html>
<html lang="en">
<head>
<meta charset="utf-8">
<title>Velvet Getaway Fest</title>
<link rel="stylesheet" href="https://fonts.googleapis.com/css2?family=Oswald:wght@700&family=Short+Stack&display=swap">
<style>
  :root {
    --frame-blue: #2fa6da;
    --panel-black: #000000;
    --panel-edge: #bfe3f3;
    --title-white: #ffffff;
    --accent-yellow: #f9c93c;
    --heart-red: #ec2027;
    --heart-deep: #c4161d;
  }
  * { margin: 0; padding: 0; box-sizing: border-box; }
  html, body {
    width: 776px;
    height: 1200px;
    overflow: hidden;
    background: var(--frame-blue);
  }
  .poster {
    position: relative;
    width: 776px;
    height: 1200px;
    background: var(--frame-blue);
  }
  .poster__panel {
    position: absolute;
    left: 32px;
    top: 33px;
    width: 705px;
    height: 1132px;
    background: var(--panel-black);
    border: 1px solid var(--panel-edge);
  }
  .poster__artwork {
    position: absolute;
    left: 181px;
    top: 440px;
    width: 414px;
    height: 326px;
  }
  .poster__title {
    position: absolute;
    left: 0;
    width: 100%;
    top: 895px;
    text-align: center;
    font-family: "Oswald", "Arial Narrow", sans-serif;
    font-weight: 700;
    font-size: 40px;
    letter-spacing: 4px;
    color: var(--title-white);
    line-height: 1;
  }
  .poster__subtitle {
    position: absolute;
    left: 0;
    width: 100%;
    top: 966px;
    text-align: center;
    font-family: "Short Stack", "Comic Sans MS", cursive;
    font-size: 34px;
    color: var(--accent-yellow);
    line-height: 1;
  }
  .poster__details {
    position: absolute;
    left: 0;
    width: 100%;
    top: 1112px;
    display: flex;
    justify-content: center;
    gap: 34px;
    font-family: "Short Stack", "Comic Sans MS", cursive;
    font-size: 24px;
    color: var(--accent-yellow);
    line-height: 1;
    white-space: nowrap;
  }
</style>
</head>
<body>
  <main class="poster">
    <div class="poster__panel"></div>

    <svg class="poster__artwork" viewBox="0 0 414 326" role="img"
         aria-label="Illustration of a red heart crossed by a pocket knife, a revolver and a pistol">
      <defs>
        <radialGradient id="heartTone" cx="50%" cy="40%" r="65%">
          <stop offset="0%" stop-color="var(--heart-red)"/>
          <stop offset="100%" stop-color="var(--heart-deep)"/>
        </radialGradient>
      </defs>
      <path fill="url(#heartTone)"
            d="M184,70 C150,10 70,0 30,40 C-10,85 10,160 60,210 L184,325 L310,210 C360,160 378,85 338,40 C298,0 218,10 184,70 Z"/>
    </svg>

    <h1 class="poster__title">VELVET GETAWAY</h1>
    <p class="poster__subtitle">fest</p>

    <p class="poster__details">
      <span class="poster__venue">Coral Lodge - Burbank, CA</span>
      <span class="poster__dates">May 2-3, 2014</span>
    </p>
  </main>
</body>
</html>
```